Publisher needs a book cover design for Enterprise Flow Study book

We need a book cover (front, back, spine) for the 3rd edition of a book entitled 'Enterprise Flow Study' and subtitled 'covering Design, Governance, Control and Growth'. The author is Marcus Thelwell. The publisher is Kestrelmoor Press. The finished size of the paperback version will be the industry standard 9" x 6". There will be paperback, hardback, and Kindle versions. The final number of pages is expected to be in the region 300-350 pages. Text for the back cover is not yet available, but at the bottom of the back cover should be publisher logo on the left and space for the ISBN bar code on the right.<br/>The design should be original and not include any stock images that have been created by someone else or may require obtaining a copyright licence to use. Symbols in common use and not copyrighted are probably ok.<br/>There are no required images, photographs or symbols except the publisher logo at the left bottom of the back cover and lower spine. S[ine lettering should be UK/US style with the top of the writing nearest the front cover. The designer is free to be creative using appropriate diagrams, symbols or abstract designs. Rectangular and circular variants of the publisher logo are attached.<br/>I just want to assure designers that when evaluating designs from my perspective, I take absolutely no notice whatsoever of a designer's Pixel Forum ranking or status; I am completely output driven, so what matters to me is the design, not the ranking or status of the designer. In a similar way, I do not evaluate designs as 'good' or 'bad' - the winning design will be chosen after review by a design panel.
Updates

More time is needed to check the use of stock images by designers. Some have been used by desitgners but not yet disclosed.

Target Market(s)

Practitioners and academics concerned with Enterprise Flow Study, Business Process Management, Business Process Architecture, Enterprise Architecture, Information Architecture, Process modelling, data modelling

Font styles to use
Serif
Sans Serif

Colors

Designer to choose colors to be used in the design.

Requirements
Must have
• Title, author, edition, subtitle, publisher logo.
Nice to have
• Originality, innovation
Should not have
• Stock images or anything else requiring additional copyright discussions and negotiations.

```html
<!DOCTYPE html>
<html lang="en">
<head>
<meta charset="utf-8">
<title>Enterprise Flow Study – Third Edition – Cover</title>
<link rel="stylesheet" href="https://fonts.googleapis.com/css2?family=Inconsolata:wdth,wght@75,400&family=Roboto+Condensed:wght@400;700&family=Cormorant+Garamond:wght@500&display=swap">
<style>
  :root {
    --paper: #ffffff;
    --ink: #111111;
    --sky: #8dd3e4;
    --sky-soft: #cdecf4;
    --rule: #222222;
  }
  html, body {
    margin: 0;
    padding: 0;
    width: 1200px;
    height: 816px;
    overflow: hidden;
    background: var(--paper);
  }
  .cover {
    position: relative;
    width: 1200px;
    height: 816px;
    background: var(--paper);
    color: var(--ink);
  }

  /* Back cover */
  .back-publisher {
    position: absolute;
    left: 22px;
    top: 748px;
    display: flex;
    align-items: center;
    gap: 8px;
    font-family: "Cormorant Garamond", serif;
    font-weight: 500;
    font-size: 19px;
    letter-spacing: 0.04em;
    color: var(--ink);
  }
  .back-publisher .mark,
  .spine-publisher .mark {
    border-radius: 50%;
    background: var(--ink);
  }
  .back-publisher .mark { width: 22px; height: 22px; }
  .isbn-space {
    position: absolute;
    left: 409px;
    top: 751px;
    font-family: "Roboto Condensed", sans-serif;
    font-weight: 700;
    font-size: 13px;
    color: var(--ink);
  }

  /* Spine */
  .spine {
    position: absolute;
    left: 538px;
    top: 0;
    width: 92px;
    height: 814px;
    border: 1px solid var(--rule);
  }
  .spine-title {
    position: absolute;
    left: 50%;
    top: 421px;
    transform: translate(-50%, -50%) rotate(-90deg) scale(1, 1.5);
    white-space: nowrap;
    font-family: "Roboto Condensed", sans-serif;
    font-weight: 400;
    font-size: 34px;
    line-height: 1;
  }
  .spine-title .edition { margin-left: 36px; }
  .spine-publisher {
    position: absolute;
    left: 0;
    right: 0;
    top: 706px;
    display: flex;
    flex-direction: column;
    align-items: center;
    gap: 6px;
    font-family: "Cormorant Garamond", serif;
    font-weight: 500;
    font-size: 13px;
    letter-spacing: 0.05em;
    text-align: center;
    line-height: 1.1;
  }
  .spine-publisher .mark { width: 16px; height: 16px; }

  /* Front cover */
  .author {
    position: absolute;
    left: 640px;
    width: 550px;
    top: 22px;
    text-align: center;
    margin: 0;
    font-family: "Roboto Condensed", sans-serif;
    font-weight: 400;
    font-size: 42px;
    letter-spacing: -0.01em;
  }
  .title,
  .subtitle {
    position: absolute;
    margin: 0;
    font-family: "Inconsolata", monospace;
    font-stretch: 75%;
    font-weight: 400;
    line-height: 1.22;
  }
  .title {
    left: 665px;
    top: 94px;
    font-size: 36px;
  }
  .subtitle {
    left: 676px;
    top: 680px;
    font-size: 37px;
  }
  .artwork {
    position: absolute;
    left: 644px;
    top: 172px;
    width: 532px;
    height: 498px;
  }
</style>
</head>
<body>
  <div class="cover">
    <section class="back-cover">
      <div class="back-publisher"><span class="mark"></span>Kestrelmoor Press</div>
      <div class="isbn-space">ISBN bar code</div>
    </section>

    <section class="spine">
      <div class="spine-title">Enterprise Flow Study<span class="edition">Third Edition</span></div>
      <div class="spine-publisher"><span class="mark"></span>Kestrelmoor<br>Press</div>
    </section>

    <section class="front-cover">
      <p class="author">Marcus Thelwell</p>
      <h1 class="title">Enterprise Flow Study<br>Third Edition</h1>
      <svg class="artwork" viewBox="0 0 532 498" role="img" aria-label="Abstract starburst of fine light-blue line fans radiating from the centre">
        <defs>
          <radialGradient id="burst" cx="50%" cy="45%" r="55%">
            <stop offset="0%" stop-color="var(--sky)"/>
            <stop offset="60%" stop-color="var(--sky-soft)"/>
            <stop offset="100%" stop-color="var(--paper)"/>
          </radialGradient>
        </defs>
        <rect width="532" height="498" fill="url(#burst)"/>
      </svg>
      <p class="subtitle">Covering Design, Governance,<br>Control and Growth.</p>
    </section>
  </div>
</body>
</html>
```